Seed Oil Safety Card for Healthy Restaurant Dining

I am seeking a design for a physical card to communicate my wife's health-related dietary restriction regarding seed oils. This card will be given to restaurant waiters to ensure her meals are prepared without seed oils, as it is a health issue and not merely a preference.
My wife cannot eat any “seed oil” or “processed oil”, including:
- Vegetable oil
- Canola oil
- Soybean oil
- Sunflower oil
- Corn oil
- Cottonseed oil
- Safflower oil
- Peanut oil
- Sesame oil
Oils that are OK for her to consume:
- Butter (most preferable)
- Extra virgin olive oil
- Avocado oil
- Coconut oil
- Ghee
- Lard
- Any other animal-based fats
Key Design Requirements:
- Clarity and speed of communication: The card should be easily read and understood by waiters, even in low-light environments, emphasizing that it's a health concern.
- Avoid common misconceptions: Ensure the design doesn't imply common dietary preferences like "vegetarian" or "no butter." Animal fats and butter are actually preferable for her!
- Preferred term: Use "seed oils" as the term to describe what she cannot eat due to her health issue.
- Trace amounts are acceptable: Communicate that it's OK to use cookware that has previously been in contact with seed oils, but not to have seed oil as an ingredient. Please suggest a concise way to convey this.
- Card dimensions: Design should be 3.5” x 2.25” (standard credit-card size on cardlomex.example). Horizontal or vertical layouts are both fine, whichever makes the message clearer.
Design Suggestions:
- Utilize bold and easy-to-read typography to communicate the main message.
- Consider incorporating relevant icons or graphics that help convey the message without adding confusion.
- Use contrasting colors to enhance readability, especially in low-light situations.
- To communicate the “trace amounts OK” part, consider phrases such as:
- "Cross-contamination acceptable"
- “Used cookware OK, no ingredient use”
- “Separate cookware not necessary”
Thank you for your assistance in creating this essential card for my wife's health and safety when dining out!

```html
<!DOCTYPE html>
<html lang="en">
<head>
<meta charset="utf-8">
<title>Seed Oil Safety Card</title>
<link rel="stylesheet" href="https://fonts.googleapis.com/css2?family=Roboto+Condensed:wght@400;700&display=swap">
<style>
  :root {
    --backdrop: #dcdcdc;
    --card-light: #fbd536;
    --card-mid: #f8c824;
    --card-deep: #f4bb1c;
    --ink: #0d0d0d;
    --band-text: #f8c826;
  }
  html, body {
    margin: 0;
    padding: 0;
    width: 1200px;
    height: 1200px;
    overflow: hidden;
    background: var(--backdrop);
  }
  .canvas { display: block; width: 1200px; height: 1200px; }
  .card-title {
    font-family: "Roboto Condensed", Arial, sans-serif;
    font-weight: 700;
    font-size: 31px;
    letter-spacing: 0.6px;
    fill: var(--ink);
  }
  .band-label {
    font-family: "Roboto Condensed", Arial, sans-serif;
    font-weight: 700;
    font-size: 22px;
    letter-spacing: 0.8px;
    fill: var(--band-text);
  }
  .item {
    font-family: "Roboto Condensed", Arial, sans-serif;
    font-weight: 700;
    font-size: 21.5px;
    letter-spacing: 0.5px;
    fill: var(--ink);
  }
  .cookware-note {
    font-family: "Roboto Condensed", Arial, sans-serif;
    font-weight: 400;
    font-size: 17.5px;
    letter-spacing: 0.3px;
    fill: var(--ink);
  }
  .box { fill: none; stroke: var(--ink); stroke-width: 2.2; }
  .mark { fill: none; stroke: var(--ink); stroke-width: 2.4; stroke-linecap: round; stroke-linejoin: round; }
  .big-mark { fill: none; stroke: var(--ink); stroke-width: 7; stroke-linecap: square; stroke-linejoin: miter; }
</style>
</head>
<body>
<svg class="canvas" viewBox="0 0 1200 1200" xmlns="http://www.w3.org/2000/svg">
  <defs>
    <linearGradient id="card-fill" x1="0" y1="0" x2="1" y2="1">
      <stop offset="0" stop-color="var(--card-light)"/>
      <stop offset="0.5" stop-color="var(--card-mid)"/>
      <stop offset="1" stop-color="var(--card-deep)"/>
    </linearGradient>
    <g id="no-box">
      <rect class="box" x="0" y="0" width="20" height="20"/>
      <path class="mark" d="M6 6 L14 14 M14 6 L6 14"/>
    </g>
    <g id="ok-box">
      <rect class="box" x="0" y="0" width="20" height="20"/>
      <path class="mark" d="M5.5 10.5 L9 14.5 L15 5"/>
    </g>
  </defs>

  <!-- card -->
  <rect class="card" x="217" y="335" width="780" height="488" rx="44" fill="url(#card-fill)"/>

  <!-- heading -->
  <text class="card-title" x="257" y="390">MY WIFE’S HEALTH AND SAFETY WHEN DINING OUT!</text>
  <rect class="title-underline" x="790" y="399" width="160" height="4" fill="var(--ink)"/>

  <!-- forbidden section band -->
  <g class="band band-forbidden">
    <rect x="330" y="432" width="570" height="46" rx="8" fill="var(--ink)"/>
    <rect x="273" y="428" width="56" height="56" fill="var(--card-mid)" stroke="var(--ink)" stroke-width="4.5"/>
    <path class="big-mark" d="M288 443 L314 469 M314 443 L288 469"/>
    <text class="band-label" x="348" y="462">Cannot Eat Any Seed Oil or Processed Oil, Including:</text>
  </g>

  <!-- forbidden oils -->
  <g class="list list-forbidden">
    <use href="#no-box" x="331" y="497"/><text class="item" x="366" y="516">Vegetable oil</text>
    <use href="#no-box" x="331" y="528"/><text class="item" x="366" y="547">Canola oil</text>
    <use href="#no-box" x="331" y="559"/><text class="item" x="366" y="578">Soybean oil</text>

    <use href="#no-box" x="545" y="498"/><text class="item" x="580" y="515">Sunflower oil</text>
    <use href="#no-box" x="545" y="529"/><text class="item" x="580" y="546">Corn oil</text>
    <use href="#no-box" x="545" y="559"/><text class="item" x="580" y="577">Cottonseed oil</text>

    <use href="#no-box" x="753" y="499"/><text class="item" x="787" y="516">Safflower oil</text>
    <use href="#no-box" x="753" y="530"/><text class="item" x="787" y="547">Peanut oil</text>
    <use href="#no-box" x="753" y="560"/><text class="item" x="787" y="578">Sesame oil</text>
  </g>

  <!-- allowed section band -->
  <g class="band band-allowed">
    <rect x="331" y="609" width="464" height="46" rx="8" fill="var(--ink)"/>
    <rect x="274" y="604" width="56" height="56" fill="var(--card-mid)" stroke="var(--ink)" stroke-width="4.5"/>
    <path class="big-mark" d="M287 634 L298 646 L317 617"/>
    <text class="band-label" x="355" y="641">Oils That Are OK For Her To Consume:</text>
  </g>

  <!-- allowed oils -->
  <g class="list list-allowed">
    <use href="#ok-box" x="334" y="674"/><text class="item" x="370" y="692">Butter (most preferable)</text>
    <use href="#ok-box" x="334" y="705"/><text class="item" x="370" y="723">Extra virgin olive oil</text>
    <use href="#ok-box" x="334" y="736"/><text class="item" x="370" y="754">Avocado oil</text>
    <use href="#ok-box" x="334" y="767"/><text class="item" x="370" y="785">Coconut oil</text>

    <use href="#ok-box" x="636" y="675"/><text class="item" x="671" y="692">Ghee</text>
    <use href="#ok-box" x="636" y="705"/><text class="item" x="671" y="723">Lard</text>
    <use href="#ok-box" x="636" y="737"/><text class="item" x="671" y="754">Any other animal-based fats</text>
  </g>

  <text class="cookware-note" x="663" y="784">“Separate cookware not necessary”</text>
</svg>
</body>
</html>
```